Electrical Contractor Company Profile

We need a Brochure that is more entertaining than our current Company Profile Document. We have lots of great experience and awesome looking jobs in our portfolio but need a document that we can either print of send in electronic format to accompany some of our submissions.

We are ideally looking for something 9-10 pages in A4 with some of the pages opening out to A3.

We are looking for a document that is professional and smart however shows the colour and quality that we feel we offer to prospective clientele.

I have included the current Company Profile and Logo along with a number of images of completed projects that may be of use.

Target Market(s)

Builders, Facility Managers, Engineers, Decision makers

Industry/Entity Type

Electrical

Font styles to use
Sans Serif

Colors

Designer to choose colors to be used in the design.

Requirements
Must have
• - Modern look with a focus on sustainability
• - Clean Simple and Professional
• - Incorporate our Logo
• Core Business Lines need to be across an A3 opening page and have photos relating to these lines Solar, Communications and any of the projects.
Nice to have
• Lots of colour and photos mixed with the text
Should not have
• Lightning bolts or corny symbols

```html
<!DOCTYPE html>
<html lang="en">
<head>
<meta charset="utf-8">
<title>Brightline Electrical – Company Profile Spreads</title>
<link href="https://fonts.googleapis.com/css2?family=Ubuntu:wght@400;500;700&display=swap" rel="stylesheet">
<style>
:root{
  --stage:#1e1e20;
  --paper:#ffffff;
  --paper-alt:#f4f4f5;
  --blue:#0d3b78;
  --blue-soft:#1f4f8e;
  --orange:#f26b1f;
  --amber:#f6a81b;
  --grey:#e3e4e6;
  --ink:#4a4a4f;
  --title:#0d3b78;
}
*{margin:0;padding:0;box-sizing:border-box}
html,body{width:1200px;height:878px;overflow:hidden;background:var(--stage)}
body{position:relative;font-family:"Ubuntu",sans-serif;color:var(--ink)}
.spread{position:absolute;width:558px;height:397px;background:var(--paper);overflow:hidden}
.spread::after{content:"";position:absolute;left:262px;top:0;width:34px;height:100%;
  background:linear-gradient(90deg,rgba(0,0,0,0) 0%,rgba(0,0,0,.07) 48%,rgba(0,0,0,.02) 52%,rgba(0,0,0,0) 100%);pointer-events:none}
.page-right{position:absolute;left:279px;top:0;width:279px;height:100%;background:var(--paper-alt)}
.abs{position:absolute}
.photo{position:absolute}
.body{font-size:4.4px;line-height:1.55;color:var(--ink)}
.body.white{color:#fff}
.just{text-align:justify}
.title{font-weight:700;color:var(--title);font-size:14px;letter-spacing:.1px}
.caps-title{font-weight:500;color:var(--title);font-size:13px}
.sub{font-weight:500;color:var(--title);font-size:7.5px;letter-spacing:.3px}
.bullets{list-style:none}
.bullets li{position:relative;padding-left:7px;font-size:4.4px;line-height:1.75}
.bullets li::before{content:"";position:absolute;left:0;top:1.6px;width:3.2px;height:3.2px;border-radius:50%;background:var(--orange)}
.bullets.right li{padding-left:0;padding-right:7px;text-align:right}
.bullets.right li::before{left:auto;right:0}
.quote{position:absolute;background:var(--blue);color:#fff;font-size:3.8px;line-height:1.4;padding:2px 6px;text-align:center}
.quote-tab{position:absolute;background:var(--amber)}
.footer-bar{position:absolute;height:8px;background:var(--grey)}
.page-no{position:absolute;width:8px;height:8px;background:var(--orange);color:#fff;font-size:4px;text-align:center;line-height:8px}
.lbl{font-weight:700;color:var(--blue)}
</style>
</head>
<body>

<!-- Spread 1: cover and summary -->
<section class="spread" style="left:22px;top:26px">
  <div class="page-right"></div>

  <div class="quote" style="left:37px;top:92px;width:226px;height:16px;display:flex;align-items:center;justify-content:center">“The final quality of workmanship on Harbourview is a reflection of the commitment that Brightline Electrical applies to all its projects.” Mark Dalton, Keystone Build</div>
  <div class="photo" role="img" aria-label="Photo of a fitted-out commercial kitchen with stainless benches and pendant lighting" style="left:22px;top:110px;width:258px;height:164px;background:linear-gradient(160deg,#7a5a3e 0%,#a48a70 35%,#cfc8c0 60%,#6c6460 100%)"></div>

  <div class="abs" style="left:22px;top:281px;width:332px;height:81px;background:var(--blue);clip-path:polygon(0 0,100% 0,91.5% 100%,0 100%)"></div>
  <div class="abs" style="left:14px;top:274px;width:64px;height:14px;background:var(--orange);color:#fff;font-size:8.5px;font-weight:500;letter-spacing:.6px;line-height:14px;padding-left:6px;border-radius:0 3px 3px 0">SUMMARY</div>
  <div class="abs body white" style="left:38px;top:293px;width:240px">
    <p style="font-size:4.8px;font-weight:500;margin-bottom:2px">Brightline Electrical is an award winning company that offers:</p>
    <ul class="bullets">
      <li>Experience with a broad range of commercial projects;</li>
      <li>An innovative approach;</li>
      <li>Experienced and knowledgeable staff;</li>
      <li>Thorough project planning;</li>
      <li>Strong operational systems;</li>
      <li>Effective communication with everyone involved in the project; and</li>
      <li>A commitment to quality workmanship.</li>
    </ul>
    <p style="margin-top:3px">We look forward to applying our skills and assisting you with your project.</p>
  </div>

  <div class="abs" style="left:297px;top:40px;display:flex;align-items:center;gap:5px">
    <span style="width:24px;height:24px;border-radius:50%;background:var(--orange)"></span>
    <span style="font-size:15px;font-weight:700;color:var(--blue);letter-spacing:.3px;line-height:1">Brightline Electrical</span>
  </div>

  <div class="photo" role="img" aria-label="Photo of a shopping arcade ceiling with yellow hexagonal lighting panels" style="left:431px;top:0;width:127px;height:102px;clip-path:polygon(40% 0,100% 0,100% 100%,0 100%);background:linear-gradient(135deg,#f7d21e 0%,#b88a10 45%,#3b3020 75%,#e6b818 100%)"></div>
  <div class="abs" style="left:279px;top:108px;width:142px;height:164px;background:var(--orange);clip-path:polygon(0 0,100% 0,49% 100%,0 100%)"></div>
  <div class="abs" style="left:300px;top:132px;color:#fff;font-size:15px;line-height:1.05;letter-spacing:.4px">COMPANY<br>PROFILE</div>
  <div class="photo" role="img" aria-label="Photo of a retail mall walkway lit by yellow honeycomb ceiling lights" style="left:352px;top:108px;width:206px;height:167px;clip-path:polygon(35% 0,100% 0,100% 100%,0 100%);background:linear-gradient(150deg,#f3c526 0%,#8a6a1a 40%,#2e2a24 70%,#caa048 100%)"></div>

  <div class="abs body" style="left:370px;top:298px;width:62px;height:20px;background:var(--grey);padding:3px 4px;font-size:3.9px">Tel. 1300 555 014<br>Email. hello@brightline-elec.com</div>
  <div class="abs body" style="left:437px;top:298px;width:102px;height:20px;background:var(--grey);padding:3px 4px;font-size:3.9px">12 Ridge Lane, Eastfield WA 6010<br>PO Box 418, Lakeview WA 6940</div>
  <div class="abs" style="left:370px;top:324px;width:169px;height:.6px;background:var(--blue)"></div>
  <p class="abs body just" style="left:370px;top:330px;width:169px;font-size:3.9px">Established in 2006, Brightline Electrical is an award winning business offering expertise across a diverse range of electrical services including commercial, industrial and communications. Brightline has the experience and capability to complete contracts for large and small along with a focus on private organisations and government agencies.</p>
  <div class="abs" style="left:370px;top:373px;font-size:8px;font-weight:700;color:var(--blue);letter-spacing:.4px">www.brightline-elec.com</div>
  <div class="abs body" style="left:480px;top:371px;width:59px;text-align:right;font-size:3.9px;color:var(--blue)">Licence No. EC 004417<br>ACN 482 316 705</div>
</section>

<!-- Spread 2: about and core business -->
<section class="spread" style="left:604px;top:26px">
  <div class="page-right"></div>

  <div class="abs" style="left:0;top:0;width:194px;height:86px;background:var(--blue);clip-path:polygon(0 0,100% 0,70% 100%,0 100%)"></div>
  <div class="abs body white" style="left:19px;top:20px;width:150px;font-size:3.9px">
    <p style="margin-bottom:3px">Established in 2006, Brightline Electrical is an award winning business offering expertise across a diverse range of electrical services including commercial, industrial and communications.</p>
    <p>Brightline has the experience and capability to complete contracts for large and small along with a focus on private organisations and government agencies. Our services include:</p>
  </div>

  <div class="photo" role="img" aria-label="Photo of a busy shopping arcade with a bright mural and ceiling lighting" style="left:0;top:86px;width:172px;height:160px;clip-path:polygon(0 0,100% 0,72% 100%,0 100%);background:linear-gradient(135deg,#c59a5a 0%,#6e5a4a 40%,#3f4b62 65%,#b07a52 100%)"></div>
  <div class="abs" style="left:128px;top:86px;width:244px;height:160px;background:var(--blue);clip-path:polygon(19.6% 0,100% 0,66.4% 100%,0 100%)"></div>
  <ul class="abs bullets right body white" style="left:168px;top:94px;width:99px;font-size:3.9px;line-height:1.85">
    <li>Electrical projects</li>
    <li>Planned and reactive maintenance</li>
    <li>Design and construct</li>
    <li>Electrical Drafting</li>
    <li>Communications</li>
    <li>Minor works</li>
    <li>Solar power generation and storage</li>
    <li>Electronic lighting control</li>
  </ul>
  <div class="abs body white" style="left:138px;top:164px;width:128px;height:68px;background:var(--blue-soft);padding:5px 6px;text-align:center;font-size:3.8px;clip-path:polygon(6% 0,100% 0,100% 100%,0 100%)">
    <p style="margin-bottom:4px">Our ability to deliver successful projects was recognised at both the 2015 &amp; 2016 State Industry Excellence Awards, in which we received awards in the Best Lighting and Best Commercial Project Category.</p>
    <p>With an office and warehouse situated centrally in Eastfield, Brightline Electrical is well placed to service the broader metropolitan area and regional areas throughout the state.</p>
  </div>

  <div class="abs" style="left:0;top:246px;width:68px;height:151px;background:var(--blue);clip-path:polygon(0 0,100% 0,30% 100%,0 100%)"></div>
  <p class="abs" style="left:150px;top:254px;width:116px;text-align:right;font-size:5px;line-height:1.4;color:var(--ink);font-weight:500">Brightline Electrical enjoys a high volume of repeat business, which is a result of our:</p>
  <ul class="abs bullets right body" style="left:140px;top:270px;width:126px;font-size:3.8px;line-height:1.5">
    <li style="margin-bottom:1.5px">commitment to consistently achieving quality results;</li>
    <li style="margin-bottom:1.5px">priority of dealing openly with our clients, staff and suppliers to begin and maintain honest, open and positive relationships;</li>
    <li style="margin-bottom:1.5px">innovation and ability to effectively source and utilise new and emerging technologies;</li>
    <li style="margin-bottom:1.5px">knowledgeable and experienced staff who have the ability to complete a range of complex projects;</li>
    <li style="margin-bottom:1.5px">team’s ability to develop designs and work systems to meet timeframes and prevent project delays; and</li>
    <li>proven approach to project management.</li>
  </ul>
  <div class="footer-bar" style="left:20px;top:379px;width:240px"></div>
  <div class="page-no" style="left:20px;top:379px">2</div>

  <div class="abs caps-title" style="left:295px;top:16px">CORE BUSINESS</div>
  <div class="abs body" style="left:295px;top:36px;width:247px;font-size:3.9px">
    <p style="margin-bottom:3px">Brightline Electrical maintains five core lines of business:</p>
    <p class="just"><span class="lbl">1. BREAKDOWN AND RESPONSE</span> – providing a 24/7 call out service to a number of high profile clients this team is high energy and responsive to most situations. Consistently performing at the top level of our clients expectations have resulted in excellent growth in this sector.</p>
  </div>
  <div class="photo" role="img" aria-label="Photo of a modern white sports institute building with curved facade and landscaping" style="left:292px;top:86px;width:266px;height:160px;clip-path:polygon(30.8% 0,100% 0,100% 100%,0 100%);background:linear-gradient(170deg,#cfe0ef 0%,#e9eef2 35%,#b9bfc4 60%,#6f7e4e 85%,#4d5a38 100%)"></div>
  <div class="abs body just" style="left:295px;top:256px;width:247px;font-size:3.9px">
    <p style="margin-bottom:3px"><span class="lbl">2. PLANNED MAINTENANCE</span> – This team service over 500 sites across the metropolitan area. Carrying out planned testing and repair of all electrical infrastructure required by our clients. This includes RCD and Emergency lighting along with thermographic surveys amongst many other services.</p>
    <p style="margin-bottom:3px"><span class="lbl">3. ELECTRICAL PROJECTS</span> – this line of business is responsible for completing contracts both considered minor and major in value. Team members are experienced in installing various types of electrical systems and are well equipped in producing the high quality workmanship expected in this highly competitive sector.</p>
    <p><span class="lbl">4. COMMUNICATIONS</span> – our staff are extremely experienced and the majority carry Open Cabling licences &amp; Certificate III qualifications in Telecommunications. The company own substantial amounts of specialised test equipment and regularly invest in continued training of staff. Our team can supply both design and installation services for private networks, providing a certified solution to any copper and fibre optic needs.</p>
  </div>
  <div class="quote-tab" style="left:530px;top:349px;width:17px;height:16px"></div>
  <div class="quote" style="left:301px;top:349px;width:230px;height:16px;display:flex;align-items:center;justify-content:center">“The finished product at the Sports Institute was of excellent quality. We were extremely impressed with the ease of use and high levels of communication we received.” Paul Reyes, Coastal Constructions</div>
  <div class="footer-bar" style="left:295px;top:379px;width:247px"></div>
  <div class="page-no" style="left:534px;top:379px">3</div>
</section>

<!-- Spread 3: solar, technology and management systems -->
<section class="spread" style="left:22px;top:440px">
  <div class="page-right"></div>

  <div class="photo" role="img" aria-label="Photo of orange electrical switchboards with meters and control panels" style="left:0;top:0;width:280px;height:180px;background:linear-gradient(120deg,#3d3a36 0%,#e2641c 30%,#f08a3a 50%,#6b6a66 75%,#c9c7c2 100%)"></div>
  <div class="abs" style="left:198px;top:136px;width:105px;height:44px;background:var(--blue);clip-path:polygon(32% 0,100% 0,100% 100%,0 100%)"></div>
  <div class="abs body just" style="left:18px;top:194px;width:246px;font-size:3.9px">
    <p style="margin-bottom:5px"><span class="lbl">5. SOLAR PV</span> – Focusing on the commercial market we are able to offer fully design solutions for photovoltaic systems up to 200KW designed to suit a client’s needs and budgets. With highly trained and experienced consultants and installers we pride ourselves on offering great value for money and clarity on project benefits.</p>
    <p><span class="lbl">6. TECHNOLOGY SERVICES</span> – With great base knowledge and an ongoing commitment to training and innovation, we are able to offer solutions for Energy Management, Energy Conservation, Electronic Lighting Control, Premises performance auditing and Power monitoring. Providing our clients with valuable expertise in reduction of running costs and better understanding of their assets maintenance requirements, producing ongoing savings in operation and replacement of plant.</p>
  </div>
  <div class="quote-tab" style="left:262px;top:308px;width:16px;height:17px"></div>
  <div class="quote" style="left:17px;top:308px;width:247px;height:17px;display:flex;align-items:center;text-align:left">“The finished product is of excellent quality, and we have been extremely impressed with the ease of use and high levels of communication received.” Lena Ward, Parkside Centre</div>
  <div class="footer-bar" style="left:17px;top:370px;width:247px"></div>
  <div class="page-no" style="left:17px;top:370px">4</div>

  <div class="abs title" style="left:293px;top:20px">Proven Management Systems</div>
  <p class="abs body" style="left:293px;top:55px;width:246px;font-size:3.9px">Our commitment to quality, health and safety and the environment places Brightline Electrical apart from our many competitors.</p>
  <div class="abs sub" style="left:293px;top:75px">QUALITY</div>
  <p class="abs body" style="left:293px;top:88px;width:246px;font-size:3.9px">Brightline Electrical is committed to providing clients with exceptional products and services in a creative and innovative manner. With our Integrated Management system aligned to ISO9001:2008 we ensure a consistent result is achieved in all cases.</p>
  <div class="abs body white" style="left:293px;top:112px;width:190px;height:100px;background:var(--blue);padding:6px 7px">
    <p style="font-size:6px;font-weight:500;margin-bottom:4px">Our Quality system ensures:</p>
    <ul class="bullets" style="font-size:3.8px">
      <li>Consistent communication with all stakeholders</li>
      <li>Experienced and qualified staff are employed who are committed to company vision and commitment to quality</li>
      <li>Flexible workforce whereby staff are able to work across all lines of business</li>
      <li>Internal systems and software that allow thorough reporting and auditing</li>
      <li>Clearly defined roles and responsibilities for all staff</li>
      <li>Correct training and support for all staff</li>
      <li>Quality monitoring and reporting throughout the entire work process</li>
    </ul>
  </div>
  <div class="photo" role="img" aria-label="Photo of a data cabinet with densely organised coloured network cabling" style="left:293px;top:224px;width:190px;height:126px;background:linear-gradient(135deg,#2a2c33 0%,#7d8794 35%,#b8a8a0 55%,#4a6a8e 75%,#22252b 100%)"></div>
  <div class="abs" style="left:488px;top:222px;width:37px;height:96px;background:var(--orange)"></div>
  <div class="abs body white" style="left:484px;top:226px;width:37px;height:96px;background:var(--blue);padding:4px;font-size:3.5px;line-height:1.45">“We found them to be professional, courteous and able to carry out their works both on time and on budget. We will be happy to use them on future projects.” Paul Reyes, Coastal Constructions</div>
  <div class="footer-bar" style="left:293px;top:370px;width:247px"></div>
  <div class="page-no" style="left:532px;top:370px">5</div>
</section>

<!-- Spread 4: environment and safety -->
<section class="spread" style="left:604px;top:440px">
  <div class="page-right"></div>

  <div class="abs title" style="left:19px;top:20px">Environment</div>
  <p class="abs body" style="left:19px;top:42px;width:246px;font-size:3.9px">Brightline Electrical works to deliver all projects in an environmentally responsible manner. We have a comprehensive set of policies and procedures that ensure we comply with all relevant environmental legislation, regulations, codes of practice and contractual conditions. We also conduct business with suppliers and sub-contractors who have a commitment to responsible environmental management.</p>

  <div class="abs" style="left:14px;top:71px;width:544px;height:169px;background:var(--blue)"></div>
  <div class="photo" role="img" aria-label="Photo of rows of rooftop solar panels under a blue sky" style="left:19px;top:76px;width:245px;height:156px;background:linear-gradient(170deg,#9fc0e0 0%,#d9e6f0 28%,#7f93ad 45%,#3e5275 70%,#a8b6c8 100%)"></div>
  <div class="photo" role="img" aria-label="Photo of a lit restaurant pavilion at dusk with outdoor lighting" style="left:294px;top:76px;width:248px;height:156px;background:linear-gradient(175deg,#1c2c4e 0%,#3b4b70 40%,#a06a3c 65%,#e0a05a 75%,#3a3a3c 100%)"></div>

  <div class="abs sub" style="left:19px;top:247px">WORKPLACE HEALTH AND SAFETY</div>
  <div class="abs body" style="left:19px;top:259px;width:246px;font-size:3.9px">
    <p style="font-weight:700;color:var(--ink);margin-bottom:2px">Our high level of safety is achieved by:</p>
    <ul class="bullets" style="font-size:3.9px;margin-bottom:4px">
      <li>Planning, developing, implementing and monitoring comprehensive health, safety and welfare programs;</li>
      <li>Promoting the understanding of health, safety and welfare as a normal component of all aspects of work;</li>
      <li>Developing site specific systems and plans to meet the requirements of each project;</li>
      <li>Ensuring staff receive appropriate safety and first aid training; and</li>
      <li>Providing a healthy and safe workplace.</li>
    </ul>
    <p style="font-weight:700;margin-bottom:2px">Brightline Electrical utilises a comprehensive HSEQ Management System, which has been developed by the State Contractors Association and tailored to suit the business, the system is:</p>
    <ul class="bullets" style="font-size:3.9px;margin-bottom:4px">
      <li>Certified to the QHSE Code: 2013; and</li>
      <li>Fully meets the requirements of AS/NZS 4801: 2001 – OHS Management Systems.</li>
    </ul>
    <p style="font-weight:700">Our system is audited twice annually to ensure that the system is being utilised</p>
  </div>
  <div class="footer-bar" style="left:19px;top:370px;width:246px"></div>
  <div class="page-no" style="left:19px;top:370px">6</div>

  <div class="quote-tab" style="left:528px;top:250px;width:15px;height:18px"></div>
  <div class="quote" style="left:302px;top:250px;width:227px;height:18px;display:flex;align-items:center;justify-content:center">“We have a long history on various projects and have been extremely satisfied with the levels of quality and customer service we have received.” Mark Dalton, Keystone Build</div>
  <div class="footer-bar" style="left:294px;top:370px;width:248px"></div>
  <div class="page-no" style="left:534px;top:370px">7</div>
</section>

</body>
</html>
```